Quill Contracting - general earthmoving business in Central Queensland

Quill Contracting is an existing company but now branching into other areas of earthmoving. We are based in Central Queensland.
We would like to use the advertisement in our local newspaper, but other areas as required.
We have attached our existing advertisement as we would like something similar, but also including our new machine and details
Industry/Entity Type
Business
Requirements
Must have
- Please include the following points:
- All general earthmoving- Dozer & Loader
- New Dams & Turkey's Nests
- Dam de-silting and repairs
- Cutter-barring
- Timber Thinning- to meet all new government regulations
- Scrub Pulling
Please also include the photos attached, OR digital images of a Loader and Dozer (as per header attached)

```html
<!DOCTYPE html>
<html lang="en">
<head>
<meta charset="UTF-8">
<title>Owen Quill Contracting – Earthmoving and Stickraking</title>
<link rel="stylesheet" href="https://fonts.googleapis.com/css2?family=Alfa+Slab+One&family=Montserrat:wght@300&family=Roboto+Condensed:wght@400;700;800;900&display=swap">
<style>
  :root {
    --black: #000000;
    --yellow: #f7c10f;
    --header-yellow: #f6c41a;
    --lime: #d4df5c;
    --white: #ffffff;
    --red: #e2231a;
    --sky: #6fb1e6;
    --sky-light: #bcdcf2;
    --ground: #8a6a45;
    --ground-dark: #5b4329;
    --machine: #eab81c;
    --machine-dark: #c9930c;
  }
  * { margin: 0; padding: 0; box-sizing: border-box; }
  html, body { width: 720px; height: 1200px; overflow: hidden; background: var(--black); }
  .ad { position: relative; width: 720px; height: 1200px; background: var(--black); overflow: hidden; }

  .masthead { position: absolute; top: 0; left: 0; width: 720px; height: 180px; text-align: center; }
  .masthead__name {
    position: absolute; top: 34px; left: 0; width: 100%;
    font-family: "Alfa Slab One", serif; font-size: 70px; line-height: 1;
    color: var(--header-yellow); letter-spacing: 1px;
  }
  .masthead__trade {
    position: absolute; top: 112px; left: 0; width: 100%;
    font-family: "Montserrat", sans-serif; font-weight: 300; font-size: 42px; line-height: 1;
    color: var(--lime); letter-spacing: 5px;
  }

  .service-band {
    position: absolute; top: 180px; left: 0; width: 720px; height: 61px;
    background: var(--yellow); display: flex; align-items: center; justify-content: center;
    font-family: "Roboto Condensed", sans-serif; font-weight: 800; font-size: 38px;
    color: var(--black); letter-spacing: 0.5px;
  }

  .hero { position: absolute; top: 241px; left: 0; width: 720px; height: 537px; }
  .hero__photo {
    position: absolute; inset: 0;
    background:
      radial-gradient(ellipse 45% 30% at 55% 42%, rgba(232,190,40,0.95), rgba(232,190,40,0) 100%),
      linear-gradient(180deg, var(--sky) 0%, var(--sky-light) 38%, var(--ground) 62%, var(--ground-dark) 100%);
  }
  .hero__kicker {
    position: absolute; top: 388px; left: 50px;
    font-family: "Roboto Condensed", sans-serif; font-weight: 800; font-size: 32px;
    color: var(--white); text-shadow: 2px 2px 4px rgba(0,0,0,0.8);
  }
  .hero__headline {
    position: absolute; top: 432px; left: 48px;
    font-family: "Roboto Condensed", sans-serif; font-weight: 900; font-size: 64px; line-height: 1;
    color: var(--white); text-shadow: 3px 3px 5px rgba(0,0,0,0.85);
  }

  .loader-image { position: absolute; top: 878px; left: 310px; width: 400px; height: 262px; }

  .services { position: absolute; top: 800px; left: 30px; width: 470px; list-style: none; }
  .services__item {
    position: relative; padding-left: 32px; margin-bottom: 15px;
    font-family: "Roboto Condensed", sans-serif; font-weight: 700; font-size: 30px; line-height: 1.3;
    color: var(--white);
  }
  .services__item::before {
    content: ""; position: absolute; left: 0; top: 12px;
    width: 17px; height: 17px; border-radius: 50%; background: var(--yellow);
  }

  .contact-bar {
    position: absolute; top: 1141px; left: 0; width: 720px; height: 59px;
    background: var(--yellow); display: flex; align-items: center; gap: 22px; padding-left: 26px;
    font-family: "Roboto Condensed", sans-serif; font-weight: 400; font-size: 23px; color: var(--black);
  }
  .contact-bar__item { display: flex; align-items: center; gap: 12px; }
  .contact-bar__item::before { content: ""; width: 12px; height: 12px; background: var(--red); }
</style>
</head>
<body>
<div class="ad">
  <header class="masthead">
    <div class="masthead__name">OWEN QUILL</div>
    <div class="masthead__trade">CONTRACTING</div>
  </header>

  <div class="service-band">EARTHMOVING AND STICKRAKING</div>

  <section class="hero">
    <div class="hero__photo" role="img" aria-label="Photo of a yellow bulldozer on cleared red-brown ground under a blue sky"></div>
    <div class="hero__kicker">ALL GENERAL EARTHMOVING</div>
    <div class="hero__headline">DOZER &amp; LOADER</div>
  </section>

  <svg class="loader-image" viewBox="0 0 400 262" role="img" aria-label="Yellow front-end wheel loader">
    <defs>
      <linearGradient id="loaderTone" x1="0" y1="0" x2="1" y2="1">
        <stop offset="0" stop-color="#f4c52a"/>
        <stop offset="0.7" stop-color="#e0a812"/>
        <stop offset="1" stop-color="#8a6a1c"/>
      </linearGradient>
    </defs>
    <path d="M200 10 Q200 0 212 0 L385 0 Q398 0 398 14 L398 230 Q398 250 378 250 L60 262 Q10 262 4 240 L0 140 Q0 122 20 122 L200 122 Z" fill="url(#loaderTone)"/>
  </svg>

  <ul class="services">
    <li class="services__item">New Dams &amp; Turkey’s Nests</li>
    <li class="services__item">Dam de-silting and repairs</li>
    <li class="services__item">Timber Thinning- to meet all new<br>government regulations</li>
    <li class="services__item">Scrub Pulling</li>
    <li class="services__item">Cutter-barring</li>
  </ul>

  <footer class="contact-bar">
    <span class="contact-bar__item">TEL : 0400 316 208</span>
    <span class="contact-bar__item">P.O.BOX 318, BRAMLEY, QLD. 4731</span>
  </footer>
</div>
</body>
</html>
```